Business Card (double-sided) and Stationary Design for dental office

1) Business Card Design: We need a business card design for a dental specialty office.
Texts should contain:
The name of our office "Maplecrest Family Orthodontics"
Tagline: "Specialist in Orthodontic and Maxillofacial Orthopedics"
Tag line: "Creating "Dorvaling" smiles for Children and Adults"
Doctor name: "Doctor Name"
Office Address:
"123 Street Name
City, State Zip code"
Office email address: office@maplecrestfamily.com
Website: www.maplecrestfamily.com

We will provide the full office address once the design is selected
Theme: beach, paradise, coastal, wave
We would like to have some creativity in design. Some acceptable ideas: front page: logo and office name. Back page: more detail information, and map to office in form of an island. Please see sample from our other location, but you DON'T HAVE TO USE OR COPY THE SAME CONCEPT.

IF POSSIBLE, PLEASE SUBMIT AT LEAST TWO CONCEPTS: ONE WITH THE BACK LOOKING SIMILAR TO WHAT IS IN THE SAMPLE, AND ONE DIFFERENT.

Color: designer to choose. We have different shade of blues and sand color in our office. Please see logo.

2) Please also design a matching set of stationary that compliment the business card and our logo.

Target Market(s)

Dental

Contact Information for Business Card

See descriptions

Font styles to use
Other font styles liked:
• Matching texts in logo

Colors
0054AA
0677BA
7BADD7
CADEEF
E8F1F8
0094D4
00A9DD
6FCCEA
C7EBF8
E9F6FB
00AB8E
00BBA5
67D7C9
C6EFE9
E9F9F6

Requirements
Must have
• Double-sided
Nice to have
• Beach coastal theme
Should not have
• Any shape or drawing of of tooth or teeth. We don’t need these. You don't necessarily have to just cut and paste the logo art and text as a whole, you have the liberty to rearrange the text.

```html
<!DOCTYPE html>
<html lang="en">
<head>
<meta charset="utf-8">
<title>Maplecrest Family Orthodontics – Business Card</title>
<link rel="stylesheet" href="https://fonts.googleapis.com/css2?family=Raleway:wght@400;500;600&family=Arimo:wght@400&display=swap">
<style>
  :root {
    --stage: #414141;
    --paper: #ffffff;
    --sand: #fdf2d6;
    --teal-deep: #2e8aa6;
    --teal: #5fc4b4;
    --sea: #5cd8c8;
    --foam: #c6e9d9;
    --ink: #1c1c1c;
    --muted: #a9a9a9;
    --palm: #6aa84f;
  }
  * { margin: 0; padding: 0; box-sizing: border-box; }
  html, body { width: 1200px; height: 801px; overflow: hidden; background: var(--stage); }
  .stage { position: relative; width: 1200px; height: 801px; }
  .card {
    position: absolute; top: 274px; width: 443px; height: 263px; overflow: hidden;
    box-shadow: 2px 2px 2px rgba(0,0,0,.75);
    font-family: "Raleway", sans-serif;
  }
  .card--front { left: 153px; background: var(--paper); }
  .card--back { left: 625px; background: var(--sand); }

  /* front */
  .brand { position: absolute; left: 20px; top: 74px; width: 196px; text-align: center; }
  .brand__mark { width: 58px; height: 58px; border-radius: 50%; background: var(--teal-deep); margin: 0 auto 8px; }
  .brand__name { font-weight: 600; font-size: 15px; line-height: 18px; color: var(--teal-deep); }
  .divider { position: absolute; left: 225px; top: 47px; width: 1px; height: 159px; background: #d9d9d9; }
  .contact { position: absolute; left: 243px; top: 64px; font-family: "Arimo", sans-serif; color: var(--ink); font-size: 12.5px; line-height: 15.5px; }
  .contact__name { font-family: "Raleway", sans-serif; font-weight: 600; font-size: 18px; line-height: 22px; color: var(--teal-deep); }
  .contact__role { margin-bottom: 11px; }
  .contact__address { margin-bottom: 11px; }
  .contact__line { display: flex; align-items: center; gap: 4px; margin-left: -1px; }
  .contact__line svg { width: 11px; height: 11px; flex: none; }
  .taglines { position: absolute; left: 0; right: 0; top: 209px; text-align: center; font-weight: 500; font-size: 12.5px; }
  .taglines__primary { color: var(--teal-deep); display: inline-block; padding-bottom: 1px; border-bottom: 1px solid var(--teal); }
  .taglines__secondary { color: var(--teal); margin-top: 1px; }

  /* back */
  .palm { position: absolute; left: 0; top: 0; width: 143px; height: 193px; background: linear-gradient(160deg, #7fc35a 0%, var(--palm) 35%, #d5a56b 75%, #e7c480 100%); opacity: .9; border-radius: 0 0 40px 0; }
  .sea { position: absolute; left: 0; top: 0; width: 443px; height: 263px; }
  .appointment { position: absolute; left: 143px; top: 20px; width: 270px; color: var(--muted); font-size: 17px; }
  .appointment__title { color: var(--teal-deep); font-weight: 500; font-size: 22px; line-height: 26px; margin-bottom: 13px; margin-left: -2px; }
  .field { border-bottom: 1px solid #c9c9c9; height: 25px; display: flex; margin-left: 2px; }
  .field + .field { margin-top: 20px; }
  .field span:nth-child(2) { margin-left: 68px; }
  .field span:nth-child(3) { margin-left: auto; }
  .map { position: absolute; left: 285px; top: 160px; width: 158px; height: 103px; background: linear-gradient(135deg, #7ee2d5, var(--sea)); }
  .pin { position: absolute; left: 328px; top: 226px; width: 12px; height: 16px; }
  .brand--back { left: 18px; top: 150px; width: 200px; }
  .brand--back .brand__mark { background: #ffffff; }
  .brand--back .brand__name { color: #ffffff; }
</style>
</head>
<body>
<main class="stage">
  <section class="card card--front">
    <div class="brand">
      <div class="brand__mark"></div>
      <div class="brand__name">Maplecrest Family<br>Orthodontics</div>
    </div>
    <div class="divider"></div>
    <div class="contact">
      <div class="contact__name">Daniel Hartwell</div>
      <div class="contact__role">Managing Director</div>
      <div class="contact__address">123 Street Name<br>City, State Zip code</div>
      <div class="contact__line">
        <svg viewBox="0 0 12 12"><rect x="0.5" y="2" width="11" height="8" fill="#2e8aa6"/><path d="M0.5 2 6 7 11.5 2" fill="none" stroke="#fff" stroke-width="1"/></svg>
        office@maplecrestfamily.com
      </div>
      <div class="contact__line">
        <svg viewBox="0 0 12 12" fill="none" stroke="#2e8aa6" stroke-width="1"><circle cx="6" cy="6" r="5"/><ellipse cx="6" cy="6" rx="2.2" ry="5"/><path d="M1 6h10M2 3.5h8M2 8.5h8"/></svg>
        www.maplecrestfamily.com
      </div>
    </div>
    <div class="taglines">
      <div class="taglines__primary">Specialist in Orthodontic and Maxillofacial Orthopedics</div>
      <div class="taglines__secondary">Creating Dorvaling smiles for Children and Adults</div>
    </div>
  </section>

  <section class="card card--back">
    <svg class="sea" viewBox="0 0 443 263" aria-hidden="true">
      <path d="M0 165 C60 150 110 140 160 150 C210 158 240 140 280 146 C330 152 370 158 400 150 C420 146 435 148 443 150 V263 H0 Z" fill="var(--foam)"/>
      <path d="M0 180 C60 168 110 158 165 170 C215 180 250 162 290 166 C340 172 380 178 415 168 C430 164 438 165 443 166 V263 H0 Z" fill="var(--sea)"/>
    </svg>
    <div class="palm" role="img" aria-label="Illustrated palm tree on a small sand island"></div>
    <div class="map" role="img" aria-label="Simple street map showing the route to the office"></div>
    <svg class="pin" viewBox="0 0 12 16" aria-hidden="true"><path d="M6 0C2.7 0 0 2.6 0 5.8 0 10 6 16 6 16s6-6 6-10.2C12 2.6 9.3 0 6 0z" fill="#1f5f73"/><circle cx="6" cy="5.8" r="2.2" fill="#5cd8c8"/></svg>
    <div class="appointment">
      <div class="appointment__title">Next Appointment</div>
      <div class="field"><span>Name</span></div>
      <div class="field"><span>Date</span><span>Time</span><span>am/pm</span></div>
    </div>
    <div class="brand brand--back">
      <div class="brand__mark"></div>
      <div class="brand__name">Maplecrest Family<br>Orthodontics</div>
    </div>
  </section>
</main>
</body>
</html>
```